ROOM REVIVE HQ
With Moira Pennell
Project: ROOM REVIVE HQ
ROOM REVIVE HQ -
Creative Brief
Use specific fonts
Not sure at the moment
Professional
Moira Pennell
Elmcroft Lodge 9 Elmcroft Terrace Hastings East Sussex TN37 6QR
moira@roomrevivehq.co.uk
www.roomrevivehq.co.uk
Company No. 5290418
Thinking of selling, about to reduce the price of your home? Before you do, speak to Moira Pennell at Room Revive HQ to see how Home Staging can help assist in selling your property fast and for the best asking price
Services Home Staging De Cluttering Moving in Moving out House Photography Sourcing accessorise

```html
<!DOCTYPE html>
<html lang="en">
<head>
<meta charset="utf-8">
<title>Room Revive HQ – Business Cards</title>
<link href="https://fonts.googleapis.com/css2?family=Open+Sans:wght@400;600&display=swap" rel="stylesheet">
<style>
  :root {
    --canvas: #ffffff;
    --edge: #b9b9b9;
    --blue: #1aa0e0;
    --blue-deep: #1d3f95;
    --blue-mid: #1f62b8;
    --pink: #e2278f;
    --purple: #5a2a6e;
    --ink: #1a1a1a;
    --ink-soft: #444444;
    --white: #ffffff;
    --logo-mark: #f0b400;
  }
  * { box-sizing: border-box; margin: 0; padding: 0; }
  html, body { width: 1200px; height: 1083px; overflow: hidden; background: var(--canvas); }
  body { position: relative; font-family: "Open Sans", Arial, sans-serif; }

  .card {
    position: absolute;
    overflow: hidden;
    border: 1px solid var(--edge);
    background: var(--white);
  }
  .card--top   { left: 272px; top: 38px;  width: 627px; height: 322px; }
  .card--front { left: 23px;  top: 375px; width: 562px; height: 322px; }
  .card--blue  { left: 600px; top: 375px; width: 571px; height: 322px;
                 background: linear-gradient(90deg, var(--blue-deep) 0%, var(--blue-mid) 55%, var(--blue) 100%); }
  .card--plain { left: 23px;  top: 711px; width: 562px; height: 322px; }
  .card--pink  { left: 600px; top: 711px; width: 571px; height: 322px;
                 background: linear-gradient(90deg, var(--pink) 0%, #a8286f 50%, var(--purple) 100%); }

  .wave { position: absolute; left: 0; top: 0; width: 100%; height: 100%; }

  .license {
    position: absolute; right: 30px; top: 16px;
    font-size: 13px; color: var(--blue-mid);
  }
  .identity { position: absolute; left: 37%; top: 38%; }
  .card--front .identity { left: 37%; top: 27%; }
  .identity__name { font-size: 25px; color: var(--blue); font-weight: 400; line-height: 1.1; }
  .identity__company { font-size: 13px; color: var(--ink); letter-spacing: 0.3px; }

  .contact {
    position: absolute; right: 28px; bottom: 22px;
    text-align: right; color: var(--white);
    font-size: 13px; line-height: 1.5; font-style: normal;
  }
  .card--front .contact { color: var(--ink-soft); }

  .logo {
    position: absolute;
    display: flex; flex-direction: column; align-items: center; gap: 8px;
    width: 140px;
  }
  .logo__mark { width: 74px; height: 74px; border-radius: 50%; background: var(--logo-mark); }
  .logo__name { font-size: 14px; font-weight: 600; color: var(--blue-deep); text-align: center; }
  .card--blue .logo__name, .card--pink .logo__name { color: var(--white); }
  .logo--front { left: 32px; top: 28px; }
  .logo--back  { right: 40px; top: 80px; }

  .services {
    position: absolute; left: 38px; top: 68px;
    list-style: none; font-size: 21px; line-height: 1.32; color: var(--white);
  }
  .card--plain .services { color: var(--ink); top: 92px; }
  .card--pink .services { left: 318px; top: 78px; }
  .card--pink .logo--back { right: auto; left: 120px; top: 90px; }
</style>
</head>
<body>

  <section class="card card--top">
    <svg class="wave" viewBox="0 0 100 100" preserveAspectRatio="none" aria-hidden="true">
      <defs>
        <linearGradient id="bandTop" x1="0" y1="0" x2="1" y2="0">
          <stop offset="0" stop-color="#1d3f95"/>
          <stop offset="1" stop-color="#1aa0e0"/>
        </linearGradient>
      </defs>
      <path d="M0,56 C30,74 60,50 100,52 L100,100 L0,100Z" fill="#dde3ee"/>
      <path d="M0,62 C30,80 60,56 100,58 L100,100 L0,100Z" fill="url(#bandTop)"/>
      <path d="M0,58 C30,76 60,52 100,54" fill="none" stroke="#e2278f" stroke-width="1.6"/>
    </svg>
    <div class="license">License No.: 5290418</div>
    <div class="logo logo--front"><span class="logo__mark"></span><span class="logo__name">ROOM REVIVE HQ</span></div>
    <div class="identity">
      <p class="identity__name">Moira Pennell</p>
      <p class="identity__company">ROOM REVIVE HQ</p>
    </div>
    <address class="contact">
      Elmcroft Lodge, 9 Elmcroft Terrace<br>
      Hastings, East Sussex TN37 6QR<br>
      Cell: 07700 900 418<br>
      Email: moira@roomrevivehq.co.uk<br>
      www.roomrevivehq.co.uk
    </address>
  </section>

  <section class="card card--front">
    <svg class="wave" viewBox="0 0 100 100" preserveAspectRatio="none" aria-hidden="true">
      <path d="M0,59 C35,71 65,49 100,43 L100,50 C65,54 35,76 0,66Z" fill="#1aa0e0"/>
      <path d="M0,56 C35,68 65,46 100,40" fill="none" stroke="#e2278f" stroke-width="1.4"/>
    </svg>
    <div class="license">License No.: 5290418</div>
    <div class="logo logo--front"><span class="logo__mark"></span><span class="logo__name">ROOM REVIVE HQ</span></div>
    <div class="identity">
      <p class="identity__name">Moira Pennell</p>
      <p class="identity__company">ROOM REVIVE HQ</p>
    </div>
    <address class="contact">
      Elmcroft Lodge, 9 Elmcroft Terrace<br>
      Hastings, East Sussex TN37 6QR<br>
      Cell: 07700 900 418<br>
      Email: moira@roomrevivehq.co.uk<br>
      www.roomrevivehq.co.uk
    </address>
  </section>

  <section class="card card--blue">
    <ul class="services">
      <li>Services</li><li>Home Staging</li><li>De Cluttering</li><li>Moving in</li>
      <li>Moving out</li><li>House Photography</li><li>Sourcing accessorise</li>
    </ul>
    <div class="logo logo--back"><span class="logo__mark"></span><span class="logo__name">ROOM REVIVE HQ</span></div>
  </section>

  <section class="card card--plain">
    <ul class="services">
      <li>Services</li><li>Home Staging</li><li>De Cluttering</li><li>Moving in</li>
      <li>Moving out</li><li>House Photography</li><li>Sourcing accessorise</li>
    </ul>
    <div class="logo logo--back"><span class="logo__mark"></span><span class="logo__name">ROOM REVIVE HQ</span></div>
  </section>

  <section class="card card--pink">
    <div class="logo logo--back"><span class="logo__mark"></span><span class="logo__name">ROOM REVIVE HQ</span></div>
    <ul class="services">
      <li>Services</li><li>Home Staging</li><li>De Cluttering</li><li>Moving in</li>
      <li>Moving out</li><li>House Photography</li><li>Sourcing accessorise</li>
    </ul>
  </section>

</body>
</html>
```